Zielgruppe
Wir sind ein ambulanter Pflegedienst, Wir versorgen hilfebedürftige Menschen. Haben sie schon Erfahrung mit ambulanten Pflegediensten?
Aufgabenstellung
Er sollte kurz und knapp sein, nicht zu viel Text.

```html
<!DOCTYPE html>
<html lang="de">
<head>
<meta charset="utf-8">
<title>Ambulante Pflege Berger &amp; Lind – Faltflyer</title>
<link rel="stylesheet" href="https://fonts.googleapis.com/css2?family=Montserrat:wght@400;500;600;700;800&display=swap">
<style>
  :root{
    --stage:#e8ecee;
    --petrol:#1d5a72;
    --petrol-light:#266b86;
    --petrol-dark:#174b60;
    --red:#d4261c;
    --white:#ffffff;
    --mark:#f0a98a;
    --photo-a:#c8703c;
    --photo-b:#8a7d5a;
    --photo-c:#5d7a4a;
  }
  *{box-sizing:border-box;margin:0;padding:0}
  html,body{width:1200px;height:848px;overflow:hidden}
  body{background:var(--stage);font-family:"Montserrat",sans-serif;color:var(--white);position:relative}

  .cover-large{position:absolute;left:280px;top:22px;width:640px;height:320px;box-shadow:0 6px 18px rgba(0,0,0,.18)}
  .spread{position:absolute;left:15px;width:1170px;height:195px;display:flex;background:var(--petrol);box-shadow:0 6px 18px rgba(0,0,0,.18);overflow:hidden}
  .spread--outside{top:368px}
  .spread--inside{top:592px;flex-direction:column;padding:10px 16px 8px 22px}
  .panel{width:390px;height:195px;position:relative;overflow:hidden;flex:none}
  .panel > svg{display:block;width:100%;height:100%}

  /* contact panel */
  .contact{padding:16px 20px 12px 28px;display:flex;flex-direction:column;gap:7px;font-size:9px;line-height:1.33}
  .contact__row{display:flex;gap:8px;align-items:flex-start}
  .contact__icon{display:block;width:10px;height:10px;flex:none;margin-top:1px}
  .contact__head{font-weight:600}

  /* inside */
  .services__title{font-size:22px;font-weight:800;letter-spacing:.5px;line-height:1.15;margin-bottom:6px}
  .services{display:flex;gap:10px;flex:1;min-height:0;padding-left:110px}
  .service{flex:1;display:flex;gap:6px;padding:0 6px 4px 0;min-width:0}
  .service:nth-child(even){background:var(--petrol-light)}
  .service__num{font-size:20px;font-weight:800;line-height:1;flex:none;width:16px}
  .service__body{flex:1;min-width:0}
  .service__head{background:var(--red);font-size:6.5px;font-weight:700;text-transform:uppercase;padding:3px 6px;line-height:1.3;margin-bottom:4px;min-height:20px;display:flex;align-items:center}
  .service__list{list-style:none;font-size:6.5px;line-height:1.2}
  .service__list li{position:relative;padding-left:11px;margin-bottom:1.3px}
  .service__list li::before{content:"";position:absolute;left:0;top:0.5px;width:6px;height:6px;border:1px solid var(--white)}
  .service__list li::after{content:"";position:absolute;left:2px;top:1px;width:2px;height:4px;border:solid var(--white);border-width:0 1px 1px 0;transform:rotate(45deg)}
  .service__note{margin-top:6px;border:1px solid var(--white);background:var(--petrol-light);font-size:6.5px;line-height:1.35;text-align:center;padding:5px 6px}
</style>
</head>
<body>

<svg width="0" height="0" style="position:absolute" aria-hidden="true">
  <defs>
    <linearGradient id="photoTone" x1="0" y1="0" x2="1" y2="1">
      <stop offset="0" stop-color="var(--photo-c)"/>
      <stop offset=".45" stop-color="var(--photo-a)"/>
      <stop offset="1" stop-color="var(--photo-b)"/>
    </linearGradient>
    <symbol id="cover" viewBox="0 0 600 300">
      <rect width="600" height="300" fill="var(--petrol)"/>
      <polygon points="342,0 600,0 462,300 228,300" fill="url(#photoTone)"/>
      <circle cx="62" cy="72" r="26" fill="var(--mark)"/>
      <text x="100" y="66" font-family="Montserrat, sans-serif" font-weight="600" font-size="21" fill="#fff">Berger &amp; Lind</text>
      <text x="100" y="92" font-family="Montserrat, sans-serif" font-weight="600" font-size="21" fill="#fff">Ambulante Pflege</text>
      <polygon points="56,150 272,150 258,202 42,202" fill="var(--red)"/>
      <text x="157" y="172" text-anchor="middle" font-family="Montserrat, sans-serif" font-weight="800" font-size="17" fill="#fff">24 STUNDEN</text>
      <text x="157" y="194" text-anchor="middle" font-family="Montserrat, sans-serif" font-weight="800" font-size="17" fill="#fff">RUFBEREITSCHAFT!</text>
    </symbol>
  </defs>
</svg>

<!-- Titelseite -->
<svg class="cover-large" viewBox="0 0 600 300" role="img" aria-label="Titelseite mit Luftaufnahme der Ortschaft mit roten Dächern"><use href="#cover"/></svg>

<!-- Außenseite -->
<section class="spread spread--outside">
  <div class="panel">
    <svg viewBox="0 0 390 195" preserveAspectRatio="none">
      <rect width="390" height="195" fill="var(--petrol)"/>
      <polygon points="0,0 372,0 352,195 0,195" fill="url(#photoTone)" role="img" aria-label="Luftaufnahme der Ortschaft mit roten Dächern"/>
    </svg>
  </div>
  <div class="panel contact">
    <div class="contact__row">
      <svg class="contact__icon" viewBox="0 0 10 10"><path d="M5 0.5a3.2 3.2 0 0 0-3.2 3.2C1.8 6 5 9.5 5 9.5S8.2 6 8.2 3.7A3.2 3.2 0 0 0 5 0.5z" fill="#fff"/><circle cx="5" cy="3.7" r="1.2" fill="var(--petrol)"/></svg>
      <div><span class="contact__head">Ambulante Pflege Berger &amp; Lind</span><br>Lindenweg 12<br>84000 Musterstadt</div>
    </div>
    <div class="contact__row">
      <svg class="contact__icon" viewBox="0 0 10 10"><path d="M2.2 0.8l1.6 1.9-0.9 1.2c.6 1.3 1.6 2.3 2.9 2.9l1.2-0.9 1.9 1.6-0.9 1.6C4.6 9 1 5.4 0.8 1.7z" fill="#fff"/></svg>
      <div>Frau Anna Berger<br>0170 1234567</div>
    </div>
    <div class="contact__row">
      <svg class="contact__icon" viewBox="0 0 10 10"><path d="M2.2 0.8l1.6 1.9-0.9 1.2c.6 1.3 1.6 2.3 2.9 2.9l1.2-0.9 1.9 1.6-0.9 1.6C4.6 9 1 5.4 0.8 1.7z" fill="#fff"/></svg>
      <div>Herr Tom Lind<br>0151 7654321</div>
    </div>
    <div class="contact__row">
      <svg class="contact__icon" viewBox="0 0 10 10"><rect x="0.8" y="2" width="8.4" height="6" fill="none" stroke="#fff"/><path d="M0.8 2L5 5.5 9.2 2" fill="none" stroke="#fff"/></svg>
      <div>E-Mail: info@pflege-bl.de</div>
    </div>
    <div class="contact__row">
      <svg class="contact__icon" viewBox="0 0 10 10"><circle cx="5" cy="5" r="4.2" fill="none" stroke="#fff"/><path d="M5 2.5V5h2" fill="none" stroke="#fff"/></svg>
      <div>Bürozeiten:<br>Mo–Fr 08:00–16:00</div>
    </div>
  </div>
  <div class="panel">
    <svg viewBox="0 0 600 300" preserveAspectRatio="none" role="img" aria-label="Titelseite mit Luftaufnahme der Ortschaft mit roten Dächern"><use href="#cover"/></svg>
  </div>
</section>

<!-- Innenseite -->
<section class="spread spread--inside">
  <h1 class="services__title">UNSERE LEISTUNGEN</h1>
  <div class="services">
    <article class="service">
      <div class="service__num">1</div>
      <div class="service__body">
        <h2 class="service__head">Grundpflege nach SGB XI</h2>
        <ul class="service__list">
          <li>Körperpflege, Duschen, Waschen, Baden, Haarpflege, Hilfe beim An- und Auskleiden, Zahnpflege, Rasieren, Nagelpflege – Hilfe bei der Nahrungsaufnahme</li>
          <li>Versorgung von Sondernahrung</li>
          <li>Stoma-Pflege</li>
          <li>Inkontinenzversorgung</li>
          <li>Lagern</li>
          <li>Mobilisieren</li>
        </ul>
      </div>
    </article>
    <article class="service">
      <div class="service__num">2</div>
      <div class="service__body">
        <h2 class="service__head">Behandlungspflege nach SGB V<br>nach ärztlicher Anordnung</h2>
        <ul class="service__list">
          <li>Moderne Wundversorgung</li>
          <li>Akute und chronische Wunden</li>
          <li>Diabetiker Behandlung</li>
          <li>Injektionen und Infusionen</li>
          <li>Blutzucker-Messung</li>
          <li>Blutdruck und Puls-Messung</li>
          <li>PEG und PEJ-Versorgung</li>
          <li>Schmerztherapie mit Schmerzpumpen</li>
          <li>Medikamentenüberwachung</li>
          <li>Medikamente verabreichen</li>
          <li>Kompressionsstrümpfe</li>
          <li>Stomaversorgung</li>
        </ul>
      </div>
    </article>
    <article class="service">
      <div class="service__num">3</div>
      <div class="service__body">
        <h2 class="service__head">Zusatzleistungen</h2>
        <ul class="service__list">
          <li>Hauswirtschaftliche Versorgung</li>
          <li>Hausnotruf durch Kooperationspartner</li>
          <li>Verhinderungspflege</li>
          <li>Entlastung von Angehörigen</li>
          <li>Essen auf Rädern</li>
          <li>24-Stunden Rufbereitschaft</li>
          <li>Beratungsbesuche nach §37 Abs. 3 SGB XI (bei Bezug von Pflegegeld)</li>
        </ul>
      </div>
    </article>
    <article class="service">
      <div class="service__num">4</div>
      <div class="service__body">
        <h2 class="service__head">Entlastungsleistungen</h2>
        <ul class="service__list">
          <li>Spaziergänge</li>
          <li>Besorgungen</li>
          <li>Hauswirtschaftliche Leistungen</li>
          <li>Betreuungsmaßnahmen</li>
        </ul>
        <p class="service__note">Der Leistungsbetrag beträgt 125 € im Monat ab Pflegegrad 1–5.</p>
      </div>
    </article>
  </div>
</section>

</body>
</html>
```